Keystone Arc Mentoring

We would like to refresh the design of our current website. We want to make it cleaner, more open and more professional looking using simple page layouts and crisp fonts. The site should be lighter and be easy to navigate.

It is important that it be easy to add and change content.

The current site can be seen at www.keystonearcmentor.example

As part of this, we want our logo colors to be darker blue and green more professional than they are currently. The current logo is attached as you can see the colors are too "neon"

THIS IS A WEBSITE DESIGN REFRESH PROJECT

Target Market(s)

Executives

Industry/Entity Type

Cleaner

Font styles to use
Sans Serif

Colors
0355a3
cfdfed
9bcb3c

Requirements
Must have
• Ease of use, ease of adding content
Should not have
• No crazy colors, not too busy...

```html
<!DOCTYPE html>
<html lang="en">
<head>
<meta charset="utf-8">
<title>Keystone Arc Mentoring</title>
<link href="https://fonts.googleapis.com/css2?family=Roboto:wght@400;500&family=Source+Sans+3:wght@400;600&display=swap" rel="stylesheet">
<style>
:root{
  --blue-deep:#0355a3;
  --blue-top:#1a8fd6;
  --blue-dark:#0a3d7a;
  --navy:#0b3a6e;
  --ink:#333;
  --green:#cde49f;
  --green-mid:#b6d47a;
  --footer:#c5dd93;
  --grey-band:#e8e8e8;
  --callout:rgba(110,120,80,.72);
  --white:#fff;
}
*{margin:0;padding:0;box-sizing:border-box}
html,body{width:1108px;height:1200px;overflow:hidden;background:var(--white)}
body{position:relative;font-family:"Source Sans 3",sans-serif;color:var(--ink)}
.abs{position:absolute}

.site-header{left:0;top:0;width:1108px;height:72px;background:linear-gradient(#1d96dc,#0a5fb0);border-top:4px solid #1b2b3a;box-shadow:0 2px 3px rgba(0,0,0,.15);z-index:3}
.brand{left:159px;top:4px;width:169px;height:101px;background:var(--white);box-shadow:0 1px 4px rgba(0,0,0,.3);z-index:4;display:flex;flex-direction:column;align-items:center;justify-content:center;gap:6px;text-align:center}
.brand-mark{width:22px;height:22px;border-radius:50%;background:var(--blue-deep)}
.brand-name{font-family:"Roboto",sans-serif;font-size:14px;color:var(--blue-deep);line-height:1.1}
.brand-tag{font-size:6px;color:var(--blue-deep);letter-spacing:.3px}
.main-nav{top:27px;left:390px;z-index:4;display:flex;font-family:"Roboto",sans-serif;font-size:13px;color:var(--white)}
.main-nav a{color:inherit;text-decoration:none;height:25px;line-height:25px;padding:0 9px;margin-right:10px}
.main-nav a.current{background:var(--white);color:#333;border-radius:4px}

.hero{left:0;top:72px;width:1108px;height:480px;background:linear-gradient(#cfe59f,#c4dd8c);overflow:hidden}
.hero-scene{left:0;top:0}
.hero-person{left:386px;top:3px;width:334px;height:470px;background:linear-gradient(#3a3f48,#20242b);border-radius:120px 120px 0 0}
.callout{height:42px;background:var(--callout);color:var(--white);font-family:"Roboto",sans-serif;font-size:20px;display:flex;align-items:center;gap:12px;padding-left:20px}
.play{width:26px;height:26px;border-radius:50%;background:#3b3b3b;border:2px solid #ddd;display:flex;align-items:center;justify-content:center}
.slide-arrow{top:205px;width:33px;height:38px;background:#3e5a44;display:flex;align-items:center;justify-content:center}
.hero-rule{left:0;top:552px;width:1108px;height:2px;background:linear-gradient(90deg,transparent,#999,transparent)}

h2{font-family:"Roboto",sans-serif;font-weight:400;color:var(--navy);font-size:20px}
.welcome{left:162px;top:608px;width:480px}
.welcome p{margin-top:12px;font-size:13px;line-height:20.5px;text-align:justify}
.more{font-size:11px;color:var(--navy);text-align:right;display:block}
.testimonials{left:687px;top:608px;width:264px}
.t-arrows{left:918px;top:610px;display:flex;gap:1px}
.t-arrows span{width:17px;height:16px;background:#111;display:flex;align-items:center;justify-content:center}
.avatar{left:678px;top:644px;width:76px;height:76px;border-radius:50%;background:linear-gradient(#8a8f98,#3a3a3e);border:4px solid #eee;box-shadow:0 0 0 1px #ccc}
.quote{left:765px;top:655px;width:186px;font-size:10.5px;line-height:16px}

.cta-band{left:154px;top:757px;width:797px;height:94px;background:var(--grey-band)}
.cta-text{left:175px;top:780px;width:480px;font-family:"Roboto",sans-serif;font-size:15.5px;line-height:25px;color:#555}
.cta-btn{left:654px;top:774px;width:274px;height:57px;background:linear-gradient(#1a8fd6,#0355a3);border-radius:4px;color:var(--white);font-family:"Roboto",sans-serif;font-size:18px;display:flex;align-items:center;justify-content:center}

.ask-title{left:159px;top:882px;font-size:18px}
.ask-img{top:940px;height:57px}
.ask-text{top:937px;width:182px;font-family:"Roboto",sans-serif;font-size:13px;line-height:19.5px;color:#444}

.site-footer{left:0;top:1047px;width:1108px;height:153px;background:var(--footer)}
.foot-nav{left:0;top:1078px;width:1108px;text-align:center;font-family:"Roboto",sans-serif;font-size:12.5px;color:#333}
.address{left:157px;top:1120px;font-family:"Roboto",sans-serif;font-size:11.5px;line-height:17.5px;color:#333}
.social{top:1119px;width:34px;height:34px;border-radius:50%;background:var(--navy)}
.copy{left:0;top:1162px;width:1108px;text-align:center;font-size:10.5px;color:#333}
</style>
</head>
<body>

<header class="site-header abs"></header>
<div class="brand abs">
  <span class="brand-mark"></span>
  <span class="brand-name">Keystone Arc Mentoring</span>
  <span class="brand-tag">Guiding leaders from struggle to strength</span>
</div>
<nav class="main-nav abs">
  <a class="current">HOME</a><a>WHY COACHING</a><a>ABOUT</a><a>SERVICES</a><a>CLIENTS</a><a>RESOURCES</a><a>CONTACT</a>
</nav>

<section class="hero abs">
  <div class="hero-scene abs" role="img" aria-label="Soft green city skyline illustration with a white rolling hill">
    <svg width="1108" height="480">
      <rect x="0" y="200" width="1108" height="280" fill="#bcd883" opacity=".5"/>
      <path d="M0 470 Q300 380 560 390 Q820 380 1108 470 L1108 480 L0 480 Z" fill="#fff"/>
    </svg>
  </div>
  <div class="hero-person abs" role="img" aria-label="Portrait of a smiling businessman in a dark suit with arms crossed"></div>

  <div class="callout abs" style="left:188px;top:180px;width:193px"><span class="play"><svg width="10" height="10"><path d="M2 0 L10 5 L2 10Z" fill="#fff"/></svg></span>ABOUT US</div>
  <div class="callout abs" style="left:738px;top:181px;width:193px;padding-left:40px"><span class="play"><svg width="10" height="10"><path d="M2 0 L10 5 L2 10Z" fill="#fff"/></svg></span>SERVICES</div>
  <div class="callout abs" style="left:159px;top:281px;width:225px"><span class="play"><svg width="10" height="10"><path d="M2 0 L10 5 L2 10Z" fill="#fff"/></svg></span>CLIENTS</div>
  <div class="callout abs" style="left:754px;top:281px;width:195px;padding-left:28px"><span class="play"><svg width="10" height="10"><path d="M2 0 L10 5 L2 10Z" fill="#fff"/></svg></span>RESOURCES</div>

  <div class="slide-arrow abs" style="left:32px"><svg width="12" height="18"><path d="M9 2 L3 9 L9 16" stroke="#fff" stroke-width="2.5" fill="none"/></svg></div>
  <div class="slide-arrow abs" style="left:1046px"><svg width="12" height="18"><path d="M3 2 L9 9 L3 16" stroke="#fff" stroke-width="2.5" fill="none"/></svg></div>
</section>
<div class="hero-rule abs"></div>

<section class="welcome abs">
  <h2>WELCOME TO KEYSTONE ARC MENTORING</h2>
  <p>Lorem ipsum dolor sit amet, consectetur adipiscing elit. Aenean nec orci urna, in pellentesque ipsum. Nam vitae odio a felis adipiscing rutrum. Maecenas sit amet tortor libero. Fusce gravida aliquet gravida. Nunc pretium, augue in ultricies pharetra, tortor nibh accumsan diam.Quisque</p>
  <a class="more">Read More &gt;&gt;</a>
</section>

<section class="testimonials abs"><h2>TESTIMONIALS</h2></section>
<div class="t-arrows abs">
  <span><svg width="8" height="10"><path d="M6 1 L2 5 L6 9" stroke="#fff" stroke-width="1.5" fill="none"/></svg></span>
  <span><svg width="8" height="10"><path d="M2 1 L6 5 L2 9" stroke="#fff" stroke-width="1.5" fill="none"/></svg></span>
</div>
<div class="avatar abs" role="img" aria-label="Round portrait of a client"></div>
<div class="quote abs">Keystone Arc Mentoring works with executives at under-performing organizations experiencing a range of issues from mild<a class="more" style="margin-top:2px">Read More &gt;&gt;</a></div>

<div class="cta-band abs"></div>
<p class="cta-text abs">Lorem Ipsum is simply dummy text of the printing and typesetting industry Lorem Ipsum has been the industry's standard dummy text</p>
<a class="cta-btn abs">REQUEST MORE INFORMATION</a>

<h2 class="ask-title abs">ASK YOURSELF</h2>
<div class="ask-img abs" style="left:154px;width:70px;background:linear-gradient(#5a9ad8,#cfe3f3 60%,#6aa83a 60%)" role="img" aria-label="Man with arms raised in a green field under a blue sky"></div>
<p class="ask-text abs" style="left:234px">Has my company lost it's momentum? Is it stuck in neutral or worse?</p>
<div class="ask-img abs" style="left:432px;width:68px;background:linear-gradient(135deg,#1d6b2a,#3faa45)" role="img" aria-label="Gauge reading toward full potential"></div>
<p class="ask-text abs" style="left:510px">Has my company lost it's momentum? Is it stuck in neutral or worse?</p>
<div class="ask-img abs" style="left:703px;width:70px;background:linear-gradient(#2a2a2a,#111)" role="img" aria-label="Stressed businessman holding his head"></div>
<p class="ask-text abs" style="left:782px">Has my company lost it's momentum? Is it stuck in neutral or worse?</p>

<footer class="site-footer abs"></footer>
<nav class="foot-nav abs">HOME &nbsp;|&nbsp; WHY COACHING &nbsp;|&nbsp; ABOUT &nbsp;|&nbsp; SERVICES &nbsp;|&nbsp; CLIENTS &nbsp;|&nbsp; RESOURCES &nbsp;|&nbsp; CONTACT</nav>
<address class="address abs" style="font-style:normal">218 Larkfield Road&nbsp; Suite 40-B&nbsp; Brentmoor, VA 20455<br>T: (555) 310-2284 &nbsp;&nbsp;&nbsp; F: (555) 310-2290</address>
<span class="social abs" style="left:790px" aria-label="Social link"></span>
<span class="social abs" style="left:832px" aria-label="Social link"></span>
<span class="social abs" style="left:872px" aria-label="Social link"></span>
<span class="social abs" style="left:914px" aria-label="Social link"></span>
<p class="copy abs">Copy Rights© 2014 Privacy Policy</p>

</body>
</html>
```